KVR Biz Cards

We are a property management company that manages luxury level residential estates. As such, we need a business card design that gives a high end feel. The idea at the moment is to list the services offered on the back of the card, and our company information on the front of the card.

Services for the back of the card are as follows:
Professional Property Management service, Home Hosting & Concierge Service, Holliday Home / Income Property Management

```html
<!DOCTYPE html>
<html lang="en">
<head>
<meta charset="utf-8">
<title>KVR Business Cards</title>
<link href="https://fonts.googleapis.com/css2?family=Arimo:wght@400;700&family=Montserrat:wght@500;600&display=swap" rel="stylesheet">
<style>
  :root {
    --stage: #2b2b2c;
    --bronze: #9a6a2c;
    --card: #ffffff;
    --card-shade: #ececec;
    --ink: #2a2a2a;
    --rule: #1d1d1d;
  }
  * { box-sizing: border-box; margin: 0; padding: 0; }
  html, body { width: 1200px; height: 900px; overflow: hidden; }
  body {
    background: var(--stage);
    font-family: "Arimo", Arial, sans-serif;
    color: var(--ink);
    display: flex;
    flex-direction: column;
    align-items: center;
    justify-content: center;
    gap: 44px;
  }
  .card {
    width: 660px;
    height: 377px;
    background: var(--bronze);
    padding: 8px;
  }
  .card-face {
    width: 100%;
    height: 100%;
    background: linear-gradient(100deg, var(--card-shade) 0%, var(--card) 55%, var(--card) 100%);
    position: relative;
  }
  .divider {
    position: absolute;
    top: 70px;
    bottom: 70px;
    width: 1.5px;
    background: var(--rule);
  }
  .brand-mark {
    display: flex;
    align-items: center;
    gap: 12px;
    font-family: "Montserrat", sans-serif;
    font-weight: 600;
    color: var(--bronze);
    letter-spacing: 2px;
  }
  .brand-square {
    width: 22px;
    height: 22px;
    background: var(--bronze);
  }

  /* Back: services */
  .back .brand-mark { position: absolute; left: 58px; top: 160px; font-size: 46px; }
  .back .divider { left: 212px; }
  .services { position: absolute; left: 252px; top: 112px; }
  .services-title {
    font-weight: 700;
    color: var(--bronze);
    font-size: 20px;
    letter-spacing: 0.5px;
    margin-bottom: 10px;
  }
  .services-list { list-style: none; }
  .services-list li {
    font-size: 16px;
    line-height: 29px;
    display: flex;
    align-items: center;
    gap: 12px;
  }
  .services-list li::before {
    content: "";
    width: 9px;
    height: 9px;
    background: var(--bronze);
    transform: rotate(45deg) scaleX(1.2);
    flex: none;
  }

  /* Front: identity and contact */
  .front .brand { position: absolute; left: 58px; top: 120px; width: 300px; }
  .front .brand-mark { font-size: 50px; margin-bottom: 14px; }
  .company-name {
    font-family: "Montserrat", sans-serif;
    font-weight: 600;
    font-size: 17px;
    letter-spacing: 0.6px;
    color: #111;
  }
  .tagline {
    font-family: "Montserrat", sans-serif;
    font-weight: 500;
    font-size: 13px;
    color: var(--bronze);
    margin-top: 2px;
  }
  .front .divider { left: 384px; }
  .contact { position: absolute; left: 418px; top: 92px; }
  .person-name { font-weight: 700; color: var(--bronze); font-size: 19px; }
  .person-role { font-size: 15px; margin-bottom: 16px; }
  .contact-list { list-style: none; font-size: 15px; }
  .contact-list li { display: flex; align-items: center; gap: 10px; line-height: 25px; }
  .contact-list svg { width: 14px; height: 14px; fill: var(--bronze); flex: none; }
  .address { display: flex; gap: 10px; margin-top: 16px; font-size: 15px; line-height: 21px; }
  .address svg { width: 14px; height: 18px; fill: var(--bronze); flex: none; margin-top: 2px; }
</style>
</head>
<body>

  <section class="card back">
    <div class="card-face">
      <div class="brand-mark"><span class="brand-square"></span>KVR</div>
      <div class="divider"></div>
      <div class="services">
        <h2 class="services-title">SERVICES</h2>
        <ul class="services-list">
          <li>Professional Property Management service</li>
          <li>Home Hosting &amp; Concierge Service</li>
          <li>Holliday Home</li>
          <li>Income Property Management</li>
        </ul>
      </div>
    </div>
  </section>

  <section class="card front">
    <div class="card-face">
      <div class="brand">
        <div class="brand-mark"><span class="brand-square"></span>KVR</div>
        <div class="company-name">KAVERN HOME MANAGEMENT</div>
        <div class="tagline">Crafted to Keep Your Home at Ease</div>
      </div>
      <div class="divider"></div>
      <div class="contact">
        <div class="person-name">DELIA VARROW</div>
        <div class="person-role">Director</div>
        <ul class="contact-list">
          <li>
            <svg viewBox="0 0 16 16" aria-hidden="true"><path d="M3 2h3l1.5 3.5-2 1.2a8 8 0 0 0 3.8 3.8l1.2-2L14 10v3a1 1 0 0 1-1 1A12 12 0 0 1 2 3a1 1 0 0 1 1-1z"/></svg>
            (00) 0000 0000
          </li>
          <li>
            <svg viewBox="0 0 16 16" aria-hidden="true"><path d="M1 3h14v10H1z M2 4l6 5 6-5" stroke="#fff" stroke-width="1"/></svg>
            delia@kvr.com
          </li>
          <li>
            <svg viewBox="0 0 16 16" aria-hidden="true"><circle cx="8" cy="8" r="7"/><path d="M1 8h14M8 1c-3 3-3 11 0 14M8 1c3 3 3 11 0 14" stroke="#fff" stroke-width="1" fill="none"/></svg>
            www.kvr.com
          </li>
        </ul>
        <div class="address">
          <svg viewBox="0 0 14 18" aria-hidden="true"><path d="M7 0a7 7 0 0 0-7 7c0 5 7 11 7 11s7-6 7-11a7 7 0 0 0-7-7zm0 10a3 3 0 1 1 0-6 3 3 0 0 1 0 6z"/></svg>
          <div>99 dummy city<br>dummy place,<br>00 Dummy Land</div>
        </div>
      </div>
    </div>
  </section>

</body>
</html>
```